Postcard flyer for body postive dance classes

We need an eye catching double sided A6 postcard for body positive dance classes. The business name is twirlbrightday and already have a rough logo and some text that needs tidying up and putting together. The design needs to be simple and elegant. We are appealing to a diverse range of adult women with or without dance experience to join us in a safe, supportive and creative environment. We would like the design to use black, white and a soft green. The final design should communicate movement, contentment and wholeness. File with information attached.

Target Market(s)

Diverse range of adult women

Industry/Entity Type

Health And Wellness

Font styles to use
Other font styles liked:
• Candara or similar but open to suggestions

Colors
abd036
cadf82
eaf2ce
fffefb
fef9ed
fff3d1
ffffff

Requirements
Must have
• Logo and text provided.
Nice to have
• Sense of movement. Match to website colours and style.
Should not have
• Intimidating perfect body images

```html
<!DOCTYPE html>
<html lang="en">
<head>
<meta charset="utf-8">
<title>twirlbrightday – Postcard Front</title>
<link rel="stylesheet" href="https://fonts.googleapis.com/css2?family=Old+Standard+TT&family=Open+Sans:wght@400&display=swap">
<style>
  :root {
    --green: #abd036;
    --paper: #ffffff;
    --ink: #555555;
    --edge: #c9c9c9;
  }
  html, body {
    margin: 0;
    padding: 0;
    width: 1200px;
    height: 851px;
    overflow: hidden;
    background: var(--paper);
  }
  .postcard {
    position: relative;
    width: 1200px;
    height: 851px;
    overflow: hidden;
    background: var(--paper);
  }
  .postcard__backdrop {
    position: absolute;
    inset: 0;
  }
  .postcard__trim {
    position: absolute;
    top: 0;
    right: 0;
    width: 0;
    height: 851px;
    border-right: 1px dashed var(--edge);
  }
  .brand {
    position: absolute;
    left: 90px;
    top: 60px;
    width: 400px;
    height: 220px;
    display: flex;
    align-items: center;
    justify-content: center;
    gap: 12px;
  }
  .brand__dot {
    width: 18px;
    height: 18px;
    border-radius: 50%;
    background: var(--ink);
  }
  .brand__name {
    font-family: "Old Standard TT", serif;
    font-weight: 400;
    font-size: 40px;
    color: var(--ink);
    letter-spacing: 0.5px;
  }
  .intro {
    position: absolute;
    left: 62px;
    top: 309px;
    width: 452px;
    margin: 0;
    font-family: "Old Standard TT", serif;
    font-size: 29px;
    line-height: 40px;
    color: var(--ink);
    text-align: justify;
    text-align-last: center;
  }
  .location {
    position: absolute;
    left: 40px;
    top: 636px;
    width: 484px;
    margin: 0;
    font-family: "Old Standard TT", serif;
    font-weight: 400;
    font-size: 40px;
    color: var(--ink);
    text-align: center;
    white-space: nowrap;
  }
  .contact {
    position: absolute;
    left: 86px;
    top: 692px;
    margin: 0;
    padding: 0;
    list-style: none;
    font-family: "Open Sans", sans-serif;
    font-size: 24px;
    color: var(--ink);
  }
  .contact__item {
    display: flex;
    align-items: center;
    height: 40px;
  }
  .contact__icon {
    width: 30px;
    height: 26px;
    margin-right: 13px;
    fill: none;
    stroke: var(--ink);
    stroke-width: 2;
  }
</style>
</head>
<body>
<main class="postcard">
  <svg class="postcard__backdrop" width="1200" height="851" viewBox="0 0 1200 851" aria-hidden="true">
    <defs>
      <linearGradient id="panel-fade" x1="0" y1="0" x2="1" y2="0">
        <stop offset="0" stop-color="#eaf2cc"/>
        <stop offset="0.45" stop-color="#f4f8e6"/>
        <stop offset="1" stop-color="#ffffff"/>
      </linearGradient>
    </defs>
    <rect width="1200" height="851" fill="var(--green)"/>
    <path d="M430,0 C250,2 70,30 28,220 C4,380 30,560 16,700 C8,800 70,835 220,832 C360,830 460,842 560,851 L1200,851 L1200,0 Z" fill="url(#panel-fade)"/>
  </svg>
  <div class="postcard__trim"></div>

  <header class="brand">
    <span class="brand__dot"></span>
    <span class="brand__name">twirlbrightday</span>
  </header>

  <p class="intro">If you’ve never danced before and always wanted to or you want to reignite your past love of dance, join us at twirlbrightday to start your journey.</p>

  <h2 class="location">Harbourside/Eastvale</h2>

  <ul class="contact">
    <li class="contact__item">
      <svg class="contact__icon" viewBox="0 0 30 26" aria-hidden="true"><rect x="2" y="5" width="26" height="17"/><path d="M2,5 L15,15 L28,5 M2,22 L12,13 M28,22 L18,13"/></svg>
      mia@twirlbrightday.com.au
    </li>
    <li class="contact__item">
      <svg class="contact__icon" viewBox="0 0 30 26" aria-hidden="true"><path d="M8,3 L12,8 L9,11 C10,15 13,18 17,19 L20,16 L25,20 L22,24 C12,23 5,15 4,6 Z"/><path d="M17,7 A5,5 0 0 1 21,11 M17,2 A10,10 0 0 1 26,11"/></svg>
      0400918274
    </li>
    <li class="contact__item">
      <svg class="contact__icon" viewBox="0 0 30 26" aria-hidden="true"><circle cx="15" cy="13" r="11"/><path d="M4,13 H26 M15,2 C9,8 9,18 15,24 M15,2 C21,8 21,18 15,24"/></svg>
      www.twirlbrightday.com.au
    </li>
  </ul>
</main>
</body>
</html>
```